Corvath - Business Card Design

Design a modern masculine business card for our business

Target Market(s)

Private Market

Industry/Entity Type

Construction

Contact Information for Business Card

Company Name - Name of Person - Address - email address - contact number

Font styles to use
Serif
Sans Serif

Colors
0094D4
00A9DD
6FCCEA
C7EBF8
E9F6FB
00AB8E
00BBA5
67D7C9
C6EFE9
E9F9F6
F0912C
F2A743
F7CA91
FBE8D2
FDF5EE

Requirements
Must have
• Use company logo provided
Nice to have
• Company Logo

```html
<!DOCTYPE html>
<html lang="en">
<head>
<meta charset="utf-8">
<title>Corvath Business Card</title>
<link href="https://fonts.googleapis.com/css2?family=Michroma&family=Arimo:wght@400&display=swap" rel="stylesheet">
<style>
  :root {
    --bg: #e6e6e6;
    --paper: #ffffff;
    --ink: #111111;
    --band: #0b0b0b;
    --orange: #ec6f24;
    --steel: #c9c9c9;
    --muted: #2a2a2a;
  }
  * { margin: 0; padding: 0; box-sizing: border-box; }
  html, body { width: 1200px; height: 1200px; overflow: hidden; background: var(--bg); }
  .canvas { position: relative; width: 1200px; height: 1200px; }
  .card {
    position: absolute; left: 150px; width: 900px; height: 514px;
    box-shadow: 0 10px 30px rgba(0,0,0,.18); overflow: hidden;
  }
  .card--front { top: 60px; background: var(--paper); }
  .card--back { top: 626px; background: var(--band); }
  .card__art { position: absolute; inset: 0; }
  .brand {
    position: absolute; display: flex; align-items: center; gap: 14px;
    font-family: "Michroma", sans-serif; letter-spacing: 1px; white-space: nowrap;
  }
  .brand__mark { background: var(--orange); flex: none; }
  .card--front .brand { left: 90px; top: 240px; font-size: 40px; color: var(--ink); }
  .card--front .brand__mark { width: 24px; height: 24px; }
  .card--back .brand { left: 0; right: 0; top: 215px; justify-content: center; font-size: 64px; color: var(--steel); }
  .card--back .brand__mark { width: 38px; height: 38px; }
  .person {
    position: absolute; left: 470px; top: 112px; white-space: nowrap;
    font-family: "Michroma", sans-serif; font-weight: 400; font-size: 34px; color: var(--ink);
  }
  .contacts {
    position: absolute; left: 480px; top: 190px; list-style: none;
    font-family: "Arimo", sans-serif; font-size: 19px; color: var(--muted);
  }
  .contacts li { display: flex; align-items: center; gap: 14px; height: 36px; white-space: nowrap; }
  .icon { width: 22px; height: 22px; flex: none; }
  .address {
    position: absolute; left: 560px; top: 337px; display: flex; align-items: center; gap: 14px;
    font-family: "Arimo", sans-serif; font-size: 19px; color: #ffffff; white-space: nowrap;
  }
</style>
</head>
<body>
<div class="canvas">
  <section class="card card--front">
    <svg class="card__art" viewBox="0 0 900 514" aria-hidden="true">
      <polygon points="530,318 900,318 900,390 490,390 470,354" fill="var(--band)"/>
      <g fill="var(--orange)">
        <polygon points="0,410 70,410 100,470 0,470"/>
        <polygon points="110,410 190,410 220,470 140,470"/>
        <polygon points="230,410 310,410 340,470 260,470"/>
        <polygon points="350,410 430,410 460,470 380,470"/>
        <polygon points="470,410 550,410 580,470 500,470"/>
      </g>
    </svg>
    <div class="brand"><span class="brand__mark"></span>Corvath</div>
    <h1 class="person">Dane Harlow</h1>
    <ul class="contacts">
      <li><svg class="icon" viewBox="0 0 22 22"><rect width="22" height="22" rx="3" fill="var(--orange)"/><path d="M7 5l3 3-1.5 1.5a7 7 0 004 4L14 12l3 3-2 2c-5 0-10-5-10-10z" fill="#fff"/></svg>555 014 227</li>
      <li><svg class="icon" viewBox="0 0 22 22"><rect width="22" height="22" rx="3" fill="var(--orange)"/><circle cx="11" cy="11" r="6" fill="none" stroke="#fff" stroke-width="1.5"/><path d="M5 11h12M11 5c-3 3-3 9 0 12M11 5c3 3 3 9 0 12" fill="none" stroke="#fff" stroke-width="1.2"/></svg>www.corvathbuild.com</li>
      <li><svg class="icon" viewBox="0 0 22 22"><rect width="22" height="22" rx="3" fill="var(--orange)"/><rect x="5" y="7" width="12" height="9" fill="none" stroke="#fff" stroke-width="1.5"/><path d="M5 7l6 5 6-5" fill="none" stroke="#fff" stroke-width="1.5"/></svg>dane@corvathbuild.com</li>
    </ul>
    <div class="address"><svg class="icon" viewBox="0 0 22 22"><rect width="22" height="22" rx="3" fill="#fff"/><path d="M11 4a5 5 0 00-5 5c0 4 5 9 5 9s5-5 5-9a5 5 0 00-5-5z" fill="var(--orange)"/><circle cx="11" cy="9" r="2" fill="#fff"/></svg>1800 N Quarry Road, Ste 12</div>
  </section>
  <section class="card card--back">
    <div class="brand"><span class="brand__mark"></span>Corvath</div>
  </section>
</div>
</body>
</html>
```